BRISKEL , FOLD LANTERN APA

Hey,

I would like to get a beer label that looks like Pemberly Guitar combo with master volume knob to show% ABV beer, beer Gain knob to show the style of APA and the Clean button to display the Best Data before. logo tag on the top of the briskel, under the middle part of Fold Lantern. lable overall dimensions are 162 millimeters wide and 90 millimeters high, the image should fit within the central part of the label area of ​​90x90 millimeters.
Attached files are easy to see my idea of label drawing , also can see my last beer label design (designed by Dale Wruton by my sketch)- a similar style I would like for the new label too.
Feel free to also create yours vision of this idea, it does not have to be exactly like my sketch. Briskel logo letters could be as in the wayward IPA label. The text could be a font of Antenna Black

Target Market(s)

craft beer drinkers, bars, pubs, beer shops etc

```html
<!DOCTYPE html>
<html lang="en">
<head>
<meta charset="utf-8">
<title>Briskel — Fold Lantern APA Label</title>
<link rel="stylesheet" href="https://fonts.googleapis.com/css2?family=Montserrat:wght@800&family=Open+Sans:wght@700&display=swap">
<style>
  :root {
    --page: #ffffff;
    --cabinet: #000000;
    --teal: #4bb3a3;
    --sun: #fed57a;
    --tomato: #e63b2e;
    --knob-light: #f2f2f2;
    --knob-dark: #8c8c8e;
    --knob-shadow: #3a3a3c;
    --grille-a: #0b0b0b;
    --grille-b: #1d1d1b;
  }
  html, body {
    margin: 0;
    padding: 0;
    width: 1200px;
    height: 999px;
    overflow: hidden;
    background: var(--page);
  }
  .label { display: block; width: 1200px; height: 999px; }
  .cabinet { fill: var(--cabinet); }
  .trim-sun { fill: var(--sun); }
  .trim-tomato { fill: var(--tomato); }
  .knob-shadow { fill: var(--knob-shadow); }
  .knob-face { fill: url(#knobShade); stroke: #ffffff; stroke-width: 2; }
  .brand-name {
    font-family: "Montserrat", "Arial Black", sans-serif;
    font-weight: 800;
    font-size: 182px;
    fill: var(--teal);
  }
  .ribbon-tail { fill: var(--teal); }
  .ribbon-fold { fill: var(--sun); }
  .ribbon-band { fill: var(--tomato); }
  .ribbon-text {
    font-family: "Open Sans", "Myriad Pro", sans-serif;
    font-weight: 700;
    font-size: 60px;
    fill: var(--sun);
  }
</style>
</head>
<body>
<svg class="label" viewBox="0 0 1200 999" xmlns="http://www.w3.org/2000/svg">
  <defs>
    <linearGradient id="knobShade" x1="0" y1="0" x2="0" y2="1">
      <stop offset="0" stop-color="var(--knob-dark)"/>
      <stop offset="1" stop-color="var(--knob-light)"/>
    </linearGradient>
    <linearGradient id="grilleShade" x1="0" y1="0" x2="1" y2="1">
      <stop offset="0" stop-color="var(--grille-b)"/>
      <stop offset="1" stop-color="var(--grille-a)"/>
    </linearGradient>
  </defs>

  <!-- amp cabinet -->
  <rect class="cabinet" x="130" y="30" width="940" height="939"/>

  <!-- control panel trim -->
  <rect class="trim-sun" x="130" y="83" width="940" height="9"/>
  <rect class="trim-tomato" x="130" y="101" width="940" height="10"/>

  <!-- control knobs -->
  <g class="knobs">
    <g transform="translate(229 0)"><ellipse class="knob-shadow" cx="2" cy="163" rx="31" ry="36"/><ellipse class="knob-face" cx="0" cy="155" rx="30" ry="33"/></g>
    <g transform="translate(322 0)"><ellipse class="knob-shadow" cx="2" cy="163" rx="31" ry="36"/><ellipse class="knob-face" cx="0" cy="155" rx="30" ry="33"/></g>
    <g transform="translate(415 0)"><ellipse class="knob-shadow" cx="2" cy="163" rx="31" ry="36"/><ellipse class="knob-face" cx="0" cy="155" rx="30" ry="33"/></g>
    <g transform="translate(507 0)"><ellipse class="knob-shadow" cx="2" cy="163" rx="31" ry="36"/><ellipse class="knob-face" cx="0" cy="155" rx="30" ry="33"/></g>
    <g transform="translate(600 0)"><ellipse class="knob-shadow" cx="2" cy="163" rx="31" ry="36"/><ellipse class="knob-face" cx="0" cy="155" rx="30" ry="33"/></g>
    <g transform="translate(693 0)"><ellipse class="knob-shadow" cx="2" cy="163" rx="31" ry="36"/><ellipse class="knob-face" cx="0" cy="155" rx="30" ry="33"/></g>
    <g transform="translate(786 0)"><ellipse class="knob-shadow" cx="2" cy="163" rx="31" ry="36"/><ellipse class="knob-face" cx="0" cy="155" rx="30" ry="33"/></g>
    <g transform="translate(878 0)"><ellipse class="knob-shadow" cx="2" cy="163" rx="31" ry="36"/><ellipse class="knob-face" cx="0" cy="155" rx="30" ry="33"/></g>
    <g transform="translate(971 0)"><ellipse class="knob-shadow" cx="2" cy="163" rx="31" ry="36"/><ellipse class="knob-face" cx="0" cy="155" rx="30" ry="33"/></g>
  </g>

  <rect class="trim-sun" x="130" y="209" width="940" height="9"/>
  <rect class="trim-tomato" x="130" y="228" width="940" height="10"/>

  <!-- speaker grille -->
  <rect x="176" y="278" width="849" height="615" fill="url(#grilleShade)" role="img" aria-label="Speaker grille cloth with fine diagonal yellow and white lines"/>

  <!-- brand name -->
  <text class="brand-name" x="188" y="425" textLength="822" lengthAdjust="spacingAndGlyphs">BRISKEL</text>

  <!-- beer name ribbon -->
  <polygon class="ribbon-tail" points="241,499 345,499 345,581 241,581 281,540"/>
  <polygon class="ribbon-fold" points="303,540 345,540 345,581"/>
  <polygon class="ribbon-tail" points="855,499 959,499 919,540 959,581 855,581"/>
  <polygon class="ribbon-fold" points="897,540 855,540 855,581"/>
  <rect class="ribbon-band" x="303" y="459" width="594" height="81"/>
  <text class="ribbon-text" x="600" y="522" text-anchor="middle">FOLD LANTERN</text>

  <!-- base trim -->
  <rect class="trim-sun" x="176" y="919" width="848" height="11"/>
  <rect class="trim-tomato" x="176" y="940" width="848" height="10"/>
</svg>
</body>
</html>
```